Alcohol drink bottle label Armenian brandy

I need a complete label for Armenian brandy in russian language АРМЯНСКИЙ КОНЬЯК 5 лет , i have bottles and labe that you can loom on it and make some better copy from it.
Should be in dark yellow and brown colors with armenian motives , symbols
Target Market(s)
Russia
Industry/Entity Type
Brandy Armenian
Font styles to use
Decorative
Colors
FFC000
F8CF3A
FAE287
FDF2CF
FEFAEE
Requirements
Must have
- Russian fonts and Armenian
Nice to have
- The product is in Green frosted bottle round shape

```html
<!DOCTYPE html>
<html lang="ru">
<head>
<meta charset="utf-8">
<title>Армянский коньяк — этикетка</title>
<link href="https://fonts.googleapis.com/css2?family=Cormorant+Garamond:wght@600;700&family=Noto+Serif+Armenian:ital,wght@0,700;1,700&display=swap" rel="stylesheet">
<style>
  :root{
    --bg:#f2f2f2;
    --gold-deep:#9a6414;
    --gold:#d9a43a;
    --gold-light:#f8cf3a;
    --gold-pale:#fae287;
    --cream:#fdf2cf;
    --maroon:#6e1a06;
    --maroon-dark:#2e0402;
    --rust:#8a2a0c;
  }
  html,body{margin:0;padding:0;overflow:hidden;}
  body{width:1200px;height:1174px;background:var(--bg);}
  .label-sheet{display:block;width:1200px;height:1174px;}
  .title-main{font-family:"Cormorant Garamond",serif;font-weight:700;fill:url(#goldText);letter-spacing:1px;}
  .title-sub{font-family:"Cormorant Garamond",serif;font-weight:700;fill:url(#goldText);letter-spacing:2px;}
  .brand-am{font-family:"Noto Serif Armenian",serif;font-style:italic;font-weight:700;fill:var(--rust);}
  .spec{font-family:"Cormorant Garamond",serif;font-weight:700;fill:var(--gold-light);}
  .age-num{font-family:"Cormorant Garamond",serif;font-weight:700;fill:var(--maroon);}
  .age-unit{font-family:"Cormorant Garamond",serif;font-weight:700;fill:var(--maroon);}
  .star{fill:var(--gold-pale);}
</style>
</head>
<body>
<svg class="label-sheet" viewBox="0 0 1200 1174" xmlns="http://www.w3.org/2000/svg">
  <defs>
    <linearGradient id="goldFrame" x1="0" y1="0" x2="1" y2="0">
      <stop offset="0" stop-color="#9a6414"/>
      <stop offset="0.25" stop-color="#f8cf3a"/>
      <stop offset="0.5" stop-color="#c88a26"/>
      <stop offset="0.75" stop-color="#fae287"/>
      <stop offset="1" stop-color="#9a6414"/>
    </linearGradient>
    <linearGradient id="ribbon" x1="0" y1="0" x2="1" y2="0">
      <stop offset="0" stop-color="#b9801f"/>
      <stop offset="0.3" stop-color="#fae287"/>
      <stop offset="0.6" stop-color="#e8b84a"/>
      <stop offset="1" stop-color="#a8701a"/>
    </linearGradient>
    <linearGradient id="panel" x1="0" y1="0" x2="0" y2="1">
      <stop offset="0" stop-color="#7a1f08"/>
      <stop offset="1" stop-color="#2e0402"/>
    </linearGradient>
    <linearGradient id="goldText" x1="0" y1="0" x2="0" y2="1">
      <stop offset="0" stop-color="#fae287"/>
      <stop offset="1" stop-color="#c88a26"/>
    </linearGradient>
    <linearGradient id="sketchFill" x1="0" y1="0" x2="0" y2="1">
      <stop offset="0" stop-color="#7a1f08"/>
      <stop offset="1" stop-color="#4a0d03"/>
    </linearGradient>
    <linearGradient id="photoFill" x1="0" y1="0" x2="0" y2="1">
      <stop offset="0" stop-color="#5d8fd0"/>
      <stop offset="0.45" stop-color="#c9b9a0"/>
      <stop offset="0.7" stop-color="#a67d5c"/>
      <stop offset="1" stop-color="#8c3d22"/>
    </linearGradient>
    <radialGradient id="medal" cx="0.5" cy="0.35" r="0.7">
      <stop offset="0" stop-color="#fdf2cf"/>
      <stop offset="0.6" stop-color="#e8b84a"/>
      <stop offset="1" stop-color="#9a6414"/>
    </radialGradient>

    <path id="labelShape" d="M100,40 Q100,12 130,12 L190,12 Q240,-8 290,12 L350,12 Q380,12 380,40 L380,90 L458,90 Q480,90 480,112 L480,262 L452,282 L452,440 Q452,470 422,470 L300,470 Q240,520 180,470 L58,470 Q28,470 28,440 L28,282 L0,262 L0,112 Q0,90 22,90 L100,90 Z"/>
    <path id="windowShape" d="M120,210 L120,55 Q120,32 145,32 L195,32 Q240,16 285,32 L335,32 Q360,32 360,55 L360,210 Z"/>

    <g id="labelBody">
      <use href="#labelShape" fill="url(#goldFrame)" stroke="#7a4a0e" stroke-width="2"/>
      <use href="#labelShape" fill="none" stroke="#fae287" stroke-width="1.5" transform="translate(12,10) scale(0.95)"/>
      <rect class="wing-ornament" x="16" y="106" width="78" height="140" rx="8" fill="#c88a26" opacity="0.55" role="img" aria-label="Орнамент с виноградной лозой"/>
      <rect class="wing-ornament" x="386" y="106" width="78" height="140" rx="8" fill="#c88a26" opacity="0.55" role="img" aria-label="Орнамент с виноградной лозой"/>

      <path class="panel" d="M48,290 L432,290 L432,438 Q432,456 414,456 L62,456 Q48,456 48,438 Z" fill="url(#panel)" stroke="#f8cf3a" stroke-width="3"/>

      <path class="ribbon-tail" d="M40,230 L10,246 L26,262 L10,280 L52,280 Z" fill="#a8701a"/>
      <path class="ribbon-tail" d="M440,230 L470,246 L454,262 L470,280 L428,280 Z" fill="#a8701a"/>
      <path class="ribbon" d="M40,214 Q240,232 440,214 L440,276 Q240,294 40,276 Z" fill="url(#ribbon)" stroke="#7a4a0e" stroke-width="1.5"/>
      <text class="brand-am" x="240" y="262" font-size="34" text-anchor="middle">Արևի Այգի</text>

      <g class="stars">
        <polygon class="star" points="150,326 153,334 161,334 155,339 157,347 150,342 143,347 145,339 139,334 147,334"/>
        <polygon class="star" points="195,322 198,331 207,331 200,337 203,346 195,341 187,346 190,337 183,331 192,331"/>
        <polygon class="star" points="240,314 244,326 257,326 247,334 251,346 240,339 229,346 233,334 223,326 236,326"/>
        <polygon class="star" points="285,322 288,331 297,331 290,337 293,346 285,341 277,346 280,337 273,331 282,331"/>
        <polygon class="star" points="330,326 333,334 341,334 335,339 337,347 330,342 323,347 325,339 319,334 327,334"/>
      </g>

      <text class="title-main" x="240" y="398" font-size="52" text-anchor="middle">АРМЯНСКИЙ</text>
      <text class="title-sub" x="240" y="432" font-size="32" text-anchor="middle">КОНЬЯК</text>

      <text class="spec" x="118" y="458" font-size="14" text-anchor="middle">40%</text>
      <text class="spec" x="118" y="472" font-size="11" text-anchor="middle">Alc.vol</text>
      <text class="spec" x="366" y="464" font-size="14" text-anchor="middle">75 cl</text>

      <ellipse class="age-medal" cx="240" cy="478" rx="72" ry="40" fill="url(#medal)" stroke="#7a4a0e" stroke-width="2"/>
      <ellipse cx="240" cy="478" rx="64" ry="33" fill="none" stroke="#fdf2cf" stroke-width="1.5"/>
      <text class="age-num" x="226" y="498" font-size="50" text-anchor="middle">5</text>
      <text class="age-unit" x="262" y="498" font-size="20" text-anchor="middle">лет</text>
    </g>
  </defs>

  <g class="label label--sketch" transform="translate(70,330)">
    <use href="#labelBody"/>
    <use href="#windowShape" fill="url(#sketchFill)" stroke="#f8cf3a" stroke-width="3" role="img" aria-label="Графический рисунок армянского монастыря в горах"/>
  </g>

  <g class="label label--photo" transform="translate(650,330)">
    <use href="#labelBody"/>
    <use href="#windowShape" fill="url(#photoFill)" stroke="#f8cf3a" stroke-width="3" role="img" aria-label="Фотография каменной крепости под голубым небом"/>
  </g>
</svg>
</body>
</html>
```